Yard Sign Design Needed

Yard sign needed for mowing & landscaping company. Would like to use the top logo with black background which is attached. Would like MOWING to be in large standout letters. The word "landscaping" can be smaller and more artistic or omitted. Will need room for phone number once design is approved. The phone number will need to stand out and look identical/similar to the word 'MOWING"

```html
<!DOCTYPE html>
<html lang="en">
<head>
<meta charset="utf-8">
<title>Marlow Contractors LLC – Mowing &amp; Landscaping Yard Sign</title>
<link rel="stylesheet" href="https://fonts.googleapis.com/css2?family=Montserrat:wght@600;700&family=Archivo+Black&family=Great+Vibes&display=swap">
<style>
  :root {
    --ink: #000000;
    --paper: #ffffff;
    --lime: #a4c93c;
    --lime-light: #b9e066;
    --olive: #7c8d10;
    --olive-dark: #5f6e0a;
    --script: #a3cc55;
  }
  html, body {
    margin: 0;
    padding: 0;
    width: 1200px;
    height: 902px;
    overflow: hidden;
    background: var(--ink);
  }
  .yard-sign {
    position: relative;
    width: 1200px;
    height: 902px;
    background: var(--ink);
    overflow: hidden;
  }
  .vine {
    position: absolute;
    border-radius: 40%;
    background: radial-gradient(circle at 40% 40%, var(--lime-light), var(--olive) 75%);
    opacity: 0.85;
  }
  .vine--left { left: 0; top: 8px; width: 152px; height: 192px; }
  .vine--right { right: 0; top: 4px; width: 196px; height: 244px; }

  .brand {
    position: absolute;
    left: 230px;
    top: 96px;
    width: 760px;
    display: flex;
    align-items: center;
    gap: 36px;
  }
  .brand__mark {
    flex: none;
    width: 150px;
    height: 150px;
    border-radius: 50%;
    background: var(--lime);
  }
  .brand__name {
    margin: 0;
    font-family: "Montserrat", sans-serif;
    font-weight: 700;
    font-size: 60px;
    line-height: 1.05;
    letter-spacing: 2px;
    color: var(--lime);
    text-transform: uppercase;
  }

  .divider {
    position: absolute;
    left: 0;
    top: 385px;
    width: 1200px;
    height: 2px;
    background: var(--olive);
  }

  .tractor {
    position: absolute;
    left: 60px;
    top: 420px;
    width: 208px;
    height: 132px;
    border-radius: 18px;
    background: linear-gradient(90deg, var(--olive), var(--lime-light));
  }

  .service, .phone-number {
    position: absolute;
    overflow: visible;
  }
  .service { left: 308px; top: 428px; width: 840px; height: 132px; }
  .service text {
    font-family: "Montserrat", sans-serif;
    font-weight: 600;
    fill: var(--paper);
  }

  .tagline {
    position: absolute;
    left: 216px;
    top: 540px;
    margin: 0;
    font-family: "Great Vibes", cursive;
    font-size: 150px;
    line-height: 1;
    color: var(--script);
  }
  .sprig {
    position: absolute;
    left: 880px;
    top: 536px;
    width: 104px;
    height: 112px;
    border-radius: 50% 50% 50% 10%;
    background: linear-gradient(135deg, var(--lime-light), var(--olive));
  }

  .grass {
    position: absolute;
    left: 0;
    top: 704px;
    width: 1200px;
    height: 40px;
    background: linear-gradient(180deg, rgba(124,141,16,0) 0%, var(--olive) 55%, var(--lime) 100%);
  }

  .contact {
    position: absolute;
    left: 0;
    top: 744px;
    width: 1200px;
    height: 158px;
    background: var(--paper);
  }
  .phone-badge {
    position: absolute;
    left: -56px;
    top: -6px;
    width: 172px;
    height: 172px;
    border-radius: 50%;
    background: linear-gradient(135deg, var(--lime), var(--olive-dark));
  }
  .phone-icon {
    position: absolute;
    left: 12px;
    top: 40px;
    width: 80px;
    height: 80px;
  }
  .phone-number { left: 140px; top: 30px; width: 1040px; height: 110px; }
  .phone-number text {
    font-family: "Archivo Black", sans-serif;
    fill: var(--ink);
  }
</style>
</head>
<body>
  <main class="yard-sign">
    <div class="vine vine--left" role="img" aria-label="Decorative green leafy vine"></div>
    <div class="vine vine--right" role="img" aria-label="Decorative green leafy vine"></div>

    <header class="brand">
      <span class="brand__mark" aria-hidden="true"></span>
      <h1 class="brand__name">Marlow<br>Contractors LLC</h1>
    </header>

    <div class="divider" aria-hidden="true"></div>

    <div class="tractor" role="img" aria-label="Green riding lawn mower illustration"></div>

    <svg class="service" viewBox="0 0 840 132" aria-label="Mowing">
      <text x="0" y="124" font-size="162" textLength="836" lengthAdjust="spacingAndGlyphs">MOWING</text>
    </svg>

    <p class="tagline">Landscaping</p>
    <div class="sprig" role="img" aria-label="Small green leaf sprig ornament"></div>

    <div class="grass" role="img" aria-label="Green grass border"></div>

    <section class="contact">
      <div class="phone-badge" aria-hidden="true"></div>
      <svg class="phone-icon" viewBox="0 0 24 24" aria-hidden="true">
        <path fill="#ffffff" d="M6.6 10.8a15.1 15.1 0 0 0 6.6 6.6l2.2-2.2a1 1 0 0 1 1-.25 11.4 11.4 0 0 0 3.6.57 1 1 0 0 1 1 1V20a1 1 0 0 1-1 1A17 17 0 0 1 3 4a1 1 0 0 1 1-1h3.5a1 1 0 0 1 1 1c0 1.25.2 2.45.57 3.6a1 1 0 0 1-.25 1z"/>
      </svg>
      <svg class="phone-number" viewBox="0 0 1040 110" aria-label="Phone 055-4821-7730">
        <text x="0" y="102" font-size="134" textLength="1036" lengthAdjust="spacingAndGlyphs">055-4821-7730</text>
      </svg>
    </section>
  </main>
</body>
</html>
```